I'm an electrician and the name of my company is called Brisk 'N' Bright Electrical. I require a professional business card that speaks to my clients, I also need it to be innovative and modern. We do maintenance & service work for domestic and commercial premises.

Industry/Entity Type

Electrical

Contact Information for Business Card

Must have the name of my company Brisk 'N' Bright Electrical, my name Darren Kolovos and my contact details 0427 381 592 and company email address Brisknbrightelectrical@mailvane.com and/or website Brisknbrightelectrical.com.au

Logo Text

Brisk 'N' Bright Electrical (If possible)

Colors
33a6d7
0592cd
3176b5

```html
<!DOCTYPE html>
<html lang="en">
<head>
<meta charset="utf-8">
<title>Brisk 'N' Bright Electrical – Business Card</title>
<link rel="stylesheet" href="https://fonts.googleapis.com/css2?family=Lato:wght@400;700;900&display=swap">
<style>
  :root {
    --stage: #e6e7e9;
    --brand-blue: #2f65aa;
    --brand-blue-light: #3176b5;
    --accent-orange: #f08a1e;
    --card-white: #ffffff;
    --ink: #3b3b3b;
    --ink-soft: #555a60;
  }
  * { margin: 0; padding: 0; box-sizing: border-box; }
  html, body { width: 1200px; height: 675px; overflow: hidden; }
  body {
    background: var(--stage);
    font-family: "Lato", Arial, sans-serif;
    display: flex;
    align-items: center;
    justify-content: center;
    gap: 60px;
  }
  .card {
    width: 500px;
    height: 286px;
    border-radius: 16px;
    position: relative;
    box-shadow: 0 6px 18px rgba(0,0,0,0.12);
    overflow: hidden;
  }

  /* Front */
  .card-front {
    background: linear-gradient(135deg, var(--brand-blue) 0%, var(--brand-blue-light) 100%);
    display: flex;
    align-items: center;
    justify-content: center;
  }
  .wordmark {
    display: flex;
    align-items: center;
    gap: 12px;
  }
  .wordmark-square {
    width: 18px;
    height: 18px;
    background: var(--accent-orange);
    flex: none;
  }
  .wordmark-name {
    font-weight: 900;
    text-transform: uppercase;
    letter-spacing: 2px;
    line-height: 1.15;
    font-size: 22px;
  }
  .card-front .wordmark-name { color: var(--card-white); }
  .card-back .wordmark-name { color: var(--brand-blue); font-size: 19px; }

  /* Back */
  .card-back {
    background: var(--card-white);
    padding: 28px 30px;
  }
  .card-back .wordmark {
    position: absolute;
    top: 48px;
    right: 34px;
  }
  .contact-list {
    list-style: none;
    display: flex;
    flex-direction: column;
    gap: 9px;
  }
  .contact-item {
    display: flex;
    align-items: center;
    gap: 9px;
    font-size: 12.5px;
    color: var(--ink);
  }
  .contact-icon {
    width: 16px;
    height: 16px;
    flex: none;
    background: var(--accent-orange);
    border-radius: 2px;
    display: flex;
    align-items: center;
    justify-content: center;
  }
  .contact-icon svg { width: 10px; height: 10px; }
  .contact-top { position: absolute; top: 30px; left: 30px; }
  .divider {
    position: absolute;
    left: 30px;
    right: 30px;
    top: 150px;
    height: 1.5px;
    background: var(--accent-orange);
  }
  .contact-bottom { position: absolute; left: 30px; bottom: 40px; }
  .person {
    position: absolute;
    right: 30px;
    bottom: 38px;
    text-align: right;
  }
  .person-name {
    font-weight: 900;
    font-size: 22px;
    letter-spacing: 1px;
    color: var(--accent-orange);
    line-height: 1;
  }
  .person-role {
    font-weight: 700;
    font-size: 11px;
    color: var(--ink-soft);
    margin-top: 3px;
  }
</style>
</head>
<body>

  <section class="card card-front" aria-label="Business card front">
    <div class="wordmark">
      <span class="wordmark-square"></span>
      <span class="wordmark-name">Brisk 'N' Bright<br>Electrical</span>
    </div>
  </section>

  <section class="card card-back" aria-label="Business card back">
    <ul class="contact-list contact-top">
      <li class="contact-item">
        <span class="contact-icon">
          <svg viewBox="0 0 10 10"><path d="M5 0.5a3 3 0 0 0-3 3c0 2.3 3 6 3 6s3-3.7 3-6a3 3 0 0 0-3-3zm0 4.2a1.2 1.2 0 1 1 0-2.4 1.2 1.2 0 0 1 0 2.4z" fill="#fff"/></svg>
        </span>
        Address Line, City, Zip code
      </li>
      <li class="contact-item">
        <span class="contact-icon">
          <svg viewBox="0 0 10 10"><path d="M2.2 0.8l1.6 1.9-0.9 1.1c0.6 1.3 1.6 2.3 2.9 2.9l1.1-0.9 1.9 1.6-1 1.6C4.3 8.8 1.2 5.7 0.8 2.2z" fill="#fff"/></svg>
        </span>
        Contact Number
      </li>
    </ul>

    <div class="wordmark">
      <span class="wordmark-square"></span>
      <span class="wordmark-name">Brisk 'N' Bright<br>Electrical</span>
    </div>

    <div class="divider"></div>

    <ul class="contact-list contact-bottom">
      <li class="contact-item">
        <span class="contact-icon">
          <svg viewBox="0 0 10 10"><rect x="0.8" y="2" width="8.4" height="6" fill="none" stroke="#fff" stroke-width="1"/><path d="M0.8 2.2L5 5.4l4.2-3.2" fill="none" stroke="#fff" stroke-width="1"/></svg>
        </span>
        Brisknbrightelectrical@mailvane.com
      </li>
      <li class="contact-item">
        <span class="contact-icon">
          <svg viewBox="0 0 10 10"><circle cx="5" cy="5" r="4" fill="none" stroke="#fff" stroke-width="1"/><path d="M1 5h8M5 1c-2 2.4-2 5.6 0 8M5 1c2 2.4 2 5.6 0 8" fill="none" stroke="#fff" stroke-width="0.8"/></svg>
        </span>
        Brisknbrightelectrical.com.au
      </li>
    </ul>

    <div class="person">
      <div class="person-name">NAME</div>
      <div class="person-role">Designation</div>
    </div>
  </section>

</body>
</html>
```